mobile app maker needs website redone

We currently have a running website that generates some traffic and looks ok but now we want to revamp it with professional modern eye catching design.
We are open to proposals and open to any new ideas or suggestions but we have to see your previous work.
our current site is www.brivelapp.com

Industry/Entity Type

It Professional

Coding

Coded - Design and coding required

Number of Pages Required

5+ page

Font styles to use
Serif
Other font styles liked:
• open

Requirements
Must have
• modern look and feel easy to use
Nice to have
• responsive websites , example are as follow ,http://quonpage-template.sitemorra.io , dalvo.com , http://marpex.sitemorra.io

```html
<!DOCTYPE html>
<html lang="en">
<head>
<meta charset="utf-8">
<title>Brivel Marketing</title>
<link rel="stylesheet" href="https://fonts.googleapis.com/css2?family=Open+Sans:wght@400;600&family=Lobster+Two:ital,wght@1,700&display=swap">
<style>
:root{
  --ink:#2f2f31;
  --dark-band:#3e3e40;
  --copy-bar:#545456;
  --light:#ffffff;
  --soft:#dcdcdc;
  --line:#cfcfcf;
  --sky-top:#1c2230;
  --sky-bottom:#0b0e16;
  --testi-bg:#f6f5f2;
  --overlay:rgba(120,120,122,.72);
  --sq-a:#3b5a94;
  --sq-b:#b0413e;
  --sq-c:#35608a;
  --sq-d:#4aa4d6;
}
*{box-sizing:border-box;margin:0;padding:0}
html,body{width:1200px;height:2325px;overflow:hidden}
body{font-family:"Open Sans",Arial,sans-serif;color:var(--ink);background:var(--light)}
.page{position:relative;width:1200px;height:2325px;overflow:hidden}
.abs{position:absolute}

.site-header{left:0;top:0;width:1200px;height:108px;background:linear-gradient(180deg,#dcdde0,#cfd0d3)}
.brand-dot{left:150px;top:18px;width:40px;height:40px;border-radius:50%;background:var(--ink)}
.brand-name{left:70px;top:64px;font-size:23px;font-weight:600;color:var(--ink)}
.main-nav a{position:absolute;top:52px;font-size:14px;color:#4a4a4c;text-decoration:none;transform:translateX(-50%);letter-spacing:.3px}
.main-nav a.active{color:#222}
.main-nav a.active::before{content:"";position:absolute;left:-4px;right:-4px;top:-9px;height:3px;background:#555}

.hero{left:0;top:108px;width:1200px;height:400px;background:radial-gradient(ellipse at 50% 30%,var(--sky-top),var(--sky-bottom))}
.hero-arrow{top:288px}

.welcome-title{left:0;width:1200px;top:562px;text-align:center;font-size:20px;font-weight:400;color:#333}
.welcome-text{left:87px;width:1032px;top:632px;font-size:12.2px;line-height:16.5px;color:#222}
.welcome-text p+p{margin-top:16px}

.services{left:0;top:771px;width:1200px;height:614px;background:var(--dark-band);color:var(--light)}
.section-title{position:absolute;left:0;width:100%;text-align:center;font-size:20px;font-weight:400}
.service{position:absolute;width:300px;text-align:center;transform:translateX(-50%)}
.service .icon{height:66px;display:flex;align-items:flex-end;justify-content:center}
.service h3{font-weight:400;font-size:17px;margin-top:10px;line-height:24px}
.service p{font-size:12.5px;line-height:17px;color:var(--soft);margin-top:30px}
.btn{position:absolute;border:3px solid var(--line);color:var(--soft);font-size:13px;text-align:center;letter-spacing:.5px;text-decoration:none}

.testimonial{left:0;top:1385px;width:1200px;height:296px;background:var(--testi-bg)}
.testimonial .section-title{top:34px;color:#333}
.testi-photo{left:0;top:79px;width:1200px;height:217px;background:linear-gradient(180deg,#e8e7e5 0%,#b9b9b9 55%,#8e8e8e 100%)}
.testi-card{left:81px;top:84px;width:1033px;height:186px;background:var(--overlay)}
.avatar{left:30px;top:30px;width:146px;height:146px;border-radius:50%;background:linear-gradient(135deg,#b98f74,#6f8fb3);border:3px solid #e9e9e9}
.quote{left:215px;top:24px;width:790px;font-family:"Lobster Two",Georgia,serif;font-style:italic;font-weight:700;font-size:38px;line-height:45px;color:var(--light)}

.clients{left:0;top:1681px;width:1200px;height:238px;background:var(--light)}
.clients .section-title{top:20px;color:#333}
.client{position:absolute;top:130px;transform:translate(-50%,-50%);font-size:32px;font-weight:600;color:#444;white-space:nowrap;display:flex;align-items:center;gap:10px}
.client i{display:block;width:26px;height:26px;border-radius:50%;background:#444}

.site-footer{left:0;top:1919px;width:1200px;height:368px;background:var(--dark-band);color:var(--light)}
.foot-head{position:absolute;top:52px;font-size:20px;font-weight:400}
.foot-about{left:101px;top:128px;width:185px;font-size:14px;line-height:18.5px}
.foot-btn{left:101px;top:225px;width:106px;height:34px;line-height:28px;font-size:10px}
.foot-nav{left:388px;top:52px;font-size:21px;line-height:26.5px}
.foot-nav a{display:block;color:var(--light);text-decoration:none}
.contact-row{position:absolute;font-size:14px;line-height:19px}
.social{position:absolute;width:53px;height:53px;border-radius:5px;display:flex;align-items:center;justify-content:center;font-size:11px;color:var(--light)}
.search{left:461px;top:267px;width:352px;height:34px;border:3px solid var(--line)}
.search span{position:absolute;left:14px;top:8px;font-size:10px;color:var(--soft)}
.search svg{position:absolute;right:8px;top:4px}
.to-top{left:1067px;top:255px;width:82px;text-align:center;font-size:13px}
.to-top svg{display:block;margin:0 auto 6px}

.copy-bar{left:0;top:2287px;width:1200px;height:38px;background:var(--copy-bar);color:var(--soft);font-size:13px;line-height:38px;padding-left:83px}
</style>
</head>
<body>
<div class="page">

  <header class="abs site-header">
    <div class="abs brand-dot"></div>
    <div class="abs brand-name">Brivel Marketing</div>
    <nav class="main-nav">
      <a class="active" href="#" style="left:580px">HOME</a>
      <a href="#" style="left:672px">FEATURES</a>
      <a href="#" style="left:765px">PRICING</a>
      <a href="#" style="left:862px">CONTACT</a>
      <a href="#" style="left:958px">SKIPPER</a>
      <a href="#" style="left:1044px">LOGIN</a>
    </nav>
  </header>

  <section class="abs hero" role="img" aria-label="Laptop, phone, watch and tablets showing app screens against a starry night sky"></section>
  <svg class="abs hero-arrow" style="left:32px" width="52" height="52" viewBox="0 0 52 52"><circle cx="26" cy="26" r="24" fill="none" stroke="#fff" stroke-width="2.5"/><path d="M31 14 L18 26 L31 38" fill="none" stroke="#fff" stroke-width="2.5"/></svg>
  <svg class="abs hero-arrow" style="left:1116px" width="52" height="52" viewBox="0 0 52 52"><circle cx="26" cy="26" r="24" fill="none" stroke="#fff" stroke-width="2.5"/><path d="M21 14 L34 26 L21 38" fill="none" stroke="#fff" stroke-width="2.5"/></svg>

  <h1 class="abs welcome-title">Welcome to our BRIVEL INC</h1>
  <div class="abs welcome-text">
    <p>Consumers use their mobile devices to find the information they want, as soon as they want it. They depend on the instant accessibility of mobile apps to quickly tell them what they need to know, so they can make their purchasing decisions and get on with what they're doing.</p>
    <p>Smart business owners understand the power and importance of mobile marketing to their bottom line. They use mobile apps to connect with customers, share relevant news, offer great deals, increase foot traffic, take reservations, and boost their revenues. Whether they deliver a service, sell products in a store, or run a successful restaurant, they know that having a mobile app is one of the most effective ways to reach their customers, whether they're on the go or standing still.</p>
  </div>

  <section class="abs services">
    <h2 class="section-title" style="top:40px">OUR SERVICES</h2>

    <div class="service" style="left:293px;top:92px">
      <div class="icon"><svg width="46" height="44" viewBox="0 0 46 44"><rect x="3" y="3" width="40" height="28" fill="none" stroke="#fff" stroke-width="4"/><rect x="19" y="31" width="8" height="6" fill="#fff"/><rect x="11" y="37" width="24" height="4" fill="#fff"/></svg></div>
      <h3>Preview Online</h3>
      <p>We allow you to preview your apps as we build it.</p>
    </div>
    <div class="service" style="left:608px;top:92px">
      <div class="icon"><svg width="46" height="44" viewBox="0 0 46 44"><path d="M4 23 L17 36 L42 9" fill="none" stroke="#fff" stroke-width="9"/></svg></div>
      <h3>Incredibly Easy</h3>
      <p>Our easy to use content manage system allows for beautiful app designs .</p>
    </div>
    <div class="service" style="left:919px;top:92px">
      <div class="icon"><svg width="50" height="48" viewBox="0 0 50 48"><rect x="2" y="2" width="46" height="12" fill="#fff"/><rect x="2" y="17" width="46" height="12" fill="#fff"/><rect x="2" y="32" width="46" height="12" fill="#fff"/><rect x="36" y="6" width="8" height="3" fill="#3e3e40"/><rect x="36" y="21" width="8" height="3" fill="#3e3e40"/><rect x="36" y="36" width="8" height="3" fill="#3e3e40"/></svg></div>
      <h3>Powerful Hosting</h3>
      <p>Our servers are hosted in the cloud using the latest hosting technology with 99.9% uptime for your apps.</p>
    </div>

    <div class="service" style="left:293px;top:300px">
      <div class="icon"><svg width="38" height="64" viewBox="0 0 40 68"><rect x="2" y="2" width="36" height="64" rx="6" fill="#fff"/><rect x="7" y="12" width="26" height="42" fill="#3e3e40"/><rect x="12" y="26" width="16" height="14" rx="3" fill="#fff"/></svg></div>
      <h3>Apps &amp; Websites</h3>
      <p>We build and create native apps for phones, tablets, &amp; every platform, and mobile websites.</p>
    </div>
    <div class="service" style="left:608px;top:300px">
      <div class="icon"><svg width="64" height="64" viewBox="0 0 68 68"><circle cx="26" cy="42" r="16" fill="none" stroke="#fff" stroke-width="7" stroke-dasharray="6 4"/><circle cx="26" cy="42" r="7" fill="none" stroke="#fff" stroke-width="4"/><circle cx="50" cy="18" r="11" fill="none" stroke="#fff" stroke-width="6" stroke-dasharray="5 3"/><circle cx="50" cy="18" r="4" fill="none" stroke="#fff" stroke-width="3"/></svg></div>
      <h3>Customize Everything</h3>
      <p>Customize every pixel inside your mobile apps within minutes using our pre-built designs or create your own.</p>
    </div>
    <div class="service" style="left:919px;top:300px">
      <div class="icon"><svg width="60" height="60" viewBox="0 0 62 62"><rect x="2" y="2" width="58" height="58" fill="#fff"/><text x="31" y="48" text-anchor="middle" font-family="Open Sans, Arial, sans-serif" font-weight="600" font-size="46" fill="#3e3e40">$</text></svg></div>
      <h3>Extremely Affordable</h3>
      <p>Is more affordable than a newspaper ad and shows a huge return on investment for businesses.</p>
    </div>

    <a class="btn" href="#" style="left:441px;top:538px;width:151px;height:48px;line-height:42px">LEARN MORE</a>
    <a class="btn" href="#" style="left:620px;top:538px;width:151px;height:48px;line-height:42px">LOG IN</a>
  </section>

  <section class="abs testimonial">
    <h2 class="section-title">TESTIMONIAL</h2>
    <div class="abs testi-photo" role="img" aria-label="Smartphone lying on a grey carpet"></div>
    <div class="abs testi-card">
      <div class="abs avatar" role="img" aria-label="Portrait of a smiling client"></div>
      <blockquote class="abs quote">“Lorem ipsum dolor sit amet, consectetur adipiscing elit. Quisque nec elit in sapien mattis ultrices tincidunt sed quam.”</blockquote>
    </div>
  </section>

  <section class="abs clients">
    <h2 class="section-title">CLIENTS</h2>
    <div class="client" style="left:171px">Hopwell</div>
    <div class="client" style="left:400px">Tarnotech</div>
    <div class="client" style="left:601px">Lumora</div>
    <div class="client" style="left:799px"><i></i>Quillby</div>
    <div class="client" style="left:1013px">Calmnest</div>
  </section>

  <footer class="abs site-footer">
    <h3 class="foot-head" style="left:101px">BRIVEL INC</h3>
    <p class="abs foot-about">A Delaware Corporation The fast &amp; easy way for small businesses to create mobile applications.</p>
    <a class="btn foot-btn" href="#">LEARN MORE</a>

    <nav class="abs foot-nav">
      <a href="#">HOME</a><a href="#">FEATURES</a><a href="#">PRICING</a><a href="#">CONTACT</a><a href="#">SKIPPER</a><a href="#">LOGIN</a>
    </nav>

    <h3 class="foot-head" style="left:617px">CONTACT US</h3>
    <div class="contact-row" style="left:586px;top:122px">ADDRESS</div>
    <div class="contact-row" style="left:690px;top:114px;width:170px">Lorem ipsum dolor sit amet, consectetur</div>
    <div class="contact-row" style="left:586px;top:164px">PHONE NO.</div>
    <div class="contact-row" style="left:690px;top:164px">1234-567-678</div>
    <div class="contact-row" style="left:586px;top:191px">EMAIL</div>
    <div class="contact-row" style="left:690px;top:191px">info@example.com</div>

    <h3 class="foot-head" style="left:939px">FOLLOW US</h3>
    <div class="social" style="left:936px;top:103px;background:var(--sq-a)">Vexo</div>
    <div class="social" style="left:997px;top:103px;background:var(--sq-b)">Pluma</div>
    <div class="social" style="left:936px;top:166px;background:var(--sq-c)">Kadro</div>
    <div class="social" style="left:997px;top:166px;background:var(--sq-d)">Sorli</div>

    <div class="abs search">
      <span>SEARCH</span>
      <svg width="22" height="22" viewBox="0 0 22 22"><circle cx="9" cy="9" r="6" fill="none" stroke="#fff" stroke-width="3"/><path d="M13.5 13.5 L19 19" stroke="#fff" stroke-width="3.5"/></svg>
    </div>

    <div class="abs to-top">
      <svg width="54" height="54" viewBox="0 0 54 54"><circle cx="27" cy="27" r="25" fill="none" stroke="#fff" stroke-width="2.5"/><path d="M17 35 L27 16 L37 35" fill="none" stroke="#fff" stroke-width="2.5"/></svg>
      Back to Top
    </div>
  </footer>

  <div class="abs copy-bar">2016 Copyright Reserved</div>
</div>
</body>
</html>
```